Travinex - You are the Boss!

Travinex is a new Silicon Valley company, of the pelim founders from Berlin, which provides a "Shared Pioneer Circle". This platform allows the crowd to support startups with money, experts and fame. Our Vision is, that everyone should become an entrepreneur.

Pls find all brief details in the attached document
Updates

Would be nice to have a list of more social services I'm available on, like a list of pictograms of all my services:

Find me on: vooka, bramlet+, qrt, fenwix, moodrail, zupp, hvoxa, etc...

pls make sure to use the right font:
http://www.typemarlow.com/fonts/Velquin

Target Market(s)

Main target market is those already involved in the startup industry, by fundraising, investing, advising, cofounding and working. Travinex brings a totaly new transparency and collaborative way of starting companies to that business.

· Entrepreneurs (looking for funding, team and community)
· Investors (looking for hot investments and )
· Experts (workers looking for startups they can work for equity)
· Incubators & Business Schools (looking for tools to advise startups)

Industry/Entity Type

It Company

Requirements
Must have
• Pls find all brief details in the attached document
Nice to have

```html
<!DOCTYPE html>
<html lang="en">
<head>
<meta charset="utf-8">
<title>Travinex – Business Card</title>
<link rel="stylesheet" href="https://fonts.googleapis.com/css2?family=Roboto+Condensed:wght@300;400&display=swap">
<style>
  :root {
    --brand-orange: #f1663b;
    --peach: #fde5d9;
    --text-grey: #8e8e8e;
    --logo-grey: #858585;
    --card-border: #bdbdbd;
    --white: #ffffff;
    --dash: #f6c3ad;
  }
  * { margin: 0; padding: 0; box-sizing: border-box; }
  html, body {
    width: 1200px; height: 901px; overflow: hidden;
    background: var(--white);
    font-family: "Roboto Condensed", "Arial Narrow", sans-serif;
    font-weight: 300;
  }
  .canvas { position: relative; width: 1200px; height: 901px; }

  .card { position: absolute; left: 261px; width: 687px; height: 387px; overflow: hidden; }
  .card--front { top: 45px; background: var(--white); border: 2px solid var(--card-border); }
  .card--back { top: 479px; background: var(--brand-orange); color: var(--white); }

  .front-decoration {
    position: absolute; left: 0; top: 0; width: 480px; height: 385px;
    background: linear-gradient(200deg, rgba(253,229,217,0.95) 0%, rgba(253,229,217,0.6) 55%, rgba(253,229,217,0) 100%);
    clip-path: polygon(0 0, 300px 0, 330px 90px, 480px 370px, 0 200px);
  }

  .contact { position: absolute; left: 30px; top: 98px; color: var(--text-grey); }
  .contact__name { font-size: 22px; line-height: 26px; }
  .contact__role { font-size: 11px; line-height: 13px; }
  .contact__lines { margin-top: 30px; font-size: 21px; line-height: 28px; }

  .social { position: absolute; left: 30px; top: 288px; list-style: none; color: var(--text-grey); font-size: 21px; line-height: 28px; }
  .social__item { display: flex; align-items: center; gap: 11px; }
  .social__mark { width: 16px; height: 16px; background: var(--text-grey); border-radius: 2px; }

  .brand { position: absolute; left: 428px; top: 58px; width: 220px; text-align: center; }
  .brand__dot { display: block; width: 46px; height: 46px; margin: 0 auto 32px; border-radius: 50%; background: var(--brand-orange); }
  .brand__name { font-size: 40px; line-height: 44px; font-weight: 400; color: var(--logo-grey); letter-spacing: 1px; }

  .back-pattern {
    position: absolute; inset: 0;
    background: linear-gradient(90deg, rgba(255,255,255,0) 0%, rgba(255,255,255,0.06) 45%, rgba(255,255,255,0.14) 100%);
  }
  .invite { position: absolute; left: 30px; top: 100px; font-size: 17px; line-height: 23.5px; }
  .notes { position: absolute; left: 30px; top: 178px; width: 371px; height: 125px; background: var(--white); }
  .notes__line { position: absolute; left: 14px; width: 338px; border-top: 1px dashed var(--dash); }
  .address { position: absolute; left: 30px; top: 318px; font-size: 17px; line-height: 24px; }
  .address__sep { margin: 0 10px; }
</style>
</head>
<body>
<main class="canvas">
  <section class="card card--front">
    <div class="front-decoration" role="img" aria-label="Large soft peach sweeping brand curves"></div>
    <div class="contact">
      <p class="contact__name">Lukas Brenner</p>
      <p class="contact__role">Founder and CEO</p>
      <div class="contact__lines">
        <p>Tel. 0198 765 432</p>
        <p>lb@travinex.com</p>
        <p>www.travinex.com</p>
      </div>
    </div>
    <ul class="social">
      <li class="social__item"><span class="social__mark"></span>Chirply.com/lukasbrenner</li>
      <li class="social__item"><span class="social__mark"></span>Friendra.com/lukasbrenner</li>
      <li class="social__item"><span class="social__mark"></span>workwyn.com/in/lukasbrenner</li>
    </ul>
    <div class="brand">
      <span class="brand__dot"></span>
      <p class="brand__name">Travinex</p>
    </div>
  </section>

  <section class="card card--back">
    <div class="back-pattern" role="img" aria-label="Repeating faint brand pattern across the orange background"></div>
    <div class="invite">
      <p>Are you interested in Startups, Investments, Work?</p>
      <p>Join: Friendra.com/Travinex</p>
      <p>QR-code -&gt; link to http://www.friendra.com/Travinex</p>
    </div>
    <div class="notes">
      <span class="notes__line" style="top:29px"></span>
      <span class="notes__line" style="top:57px"></span>
      <span class="notes__line" style="top:84px"></span>
      <span class="notes__line" style="top:112px"></span>
    </div>
    <div class="address">
      <p>Berlin - Lindenhof Allee 12<span class="address__sep">|</span>10117 Berlin<span class="address__sep">|</span>Germany</p>
      <p>Silicon Valley - 215 Harlow Ave<span class="address__sep">|</span>Sunnyvale<span class="address__sep">|</span>CA 94086</p>
    </div>
  </section>
</main>
</body>
</html>
```